Velmarine - Mechanic/Collision Center Business Card

We're looking for a business card design for our mechanic/ collision repair shop.

Can be with colours or monochromatic.

See the attached files.

Many thanks

```html
<!DOCTYPE html>
<html lang="en">
<head>
<meta charset="UTF-8">
<title>Velmarine – Business Card</title>
<link href="https://fonts.googleapis.com/css2?family=Work+Sans:wght@400;500;700;800&display=swap" rel="stylesheet">
<style>
  :root {
    --stage: #2b2b2b;
    --card: #1f1f1f;
    --card-edge: #262626;
    --ink: #f2f2f2;
    --ink-soft: #d9d9d9;
    --accent: #2aa3df;
    --emboss: #4d4d4d;
  }
  * { box-sizing: border-box; margin: 0; padding: 0; }
  html, body {
    width: 1200px; height: 900px; overflow: hidden;
    background: var(--stage);
    font-family: "Work Sans", Arial, sans-serif;
  }
  .stage {
    width: 1200px; height: 900px;
    display: flex; flex-direction: column; align-items: center; justify-content: center;
    gap: 36px;
  }
  .card {
    width: 700px; height: 400px;
    background: linear-gradient(160deg, var(--card-edge), var(--card));
    box-shadow: 0 14px 30px rgba(0,0,0,.45);
    position: relative;
  }
  /* back side */
  .card--back { display: flex; align-items: center; justify-content: center; }
  .wordmark--embossed {
    font-weight: 800; font-size: 64px; letter-spacing: 1px;
    color: var(--emboss);
  }
  /* front side */
  .card--front { display: flex; align-items: center; }
  .brand {
    width: 390px; display: flex; align-items: center; justify-content: center; gap: 14px;
  }
  .brand__dot { width: 26px; height: 26px; border-radius: 50%; background: var(--accent); }
  .brand__name { font-weight: 800; font-size: 50px; color: var(--ink); }
  .divider { width: 2px; height: 230px; background: var(--accent); }
  .contact { padding-left: 34px; color: var(--ink-soft); }
  .contact__name { color: var(--accent); font-weight: 500; font-size: 30px; line-height: 1; }
  .contact__role { font-size: 19px; margin-top: 4px; }
  .contact__address { font-size: 19px; line-height: 1.35; margin-top: 18px; }
  .contact__list { list-style: none; margin-top: 14px; font-size: 19px; line-height: 1.55; }
  .contact__list li { display: flex; align-items: center; gap: 10px; }
  .contact__list svg { width: 14px; height: 14px; flex: none; }
  .highlight { color: var(--accent); }
</style>
</head>
<body>
<main class="stage">
  <section class="card card--back">
    <div class="wordmark--embossed">Velmarine</div>
  </section>

  <section class="card card--front">
    <div class="brand">
      <span class="brand__dot"></span>
      <span class="brand__name">Velmarine</span>
    </div>
    <div class="divider"></div>
    <div class="contact">
      <div class="contact__name">DARREN HOLT</div>
      <div class="contact__role">Director</div>
      <div class="contact__address">418 Birch Hollow Lane<br>Millbrook, PA 19330</div>
      <ul class="contact__list">
        <li>
          <svg viewBox="0 0 16 16" fill="none" stroke="#2aa3df" stroke-width="1.6"><path d="M4 1.5l2 3-1.5 1.5c.8 2 2.5 3.7 4.5 4.5L10.5 9l3 2-1.2 2.5C7 13 3 9 2.5 3.2z"/></svg>
          06.41.73.20.85
        </li>
        <li>
          <svg viewBox="0 0 16 16" fill="none" stroke="#2aa3df" stroke-width="1.6"><rect x="1.5" y="3.5" width="13" height="9"/><path d="M1.5 3.5L8 9l6.5-5.5"/></svg>
          info@velmarine.com
        </li>
        <li>
          <svg viewBox="0 0 16 16" fill="none" stroke="#2aa3df" stroke-width="1.4"><circle cx="8" cy="8" r="6.5"/><ellipse cx="8" cy="8" rx="3" ry="6.5"/><path d="M1.5 8h13"/></svg>
          <span>www.<span class="highlight">velmarine</span>.com</span>
        </li>
      </ul>
    </div>
  </section>
</main>
</body>
</html>
```